brovalux business card

We are a commercial cleaning/janitorial service company our main target is building owners and managers.
Would like to see the icon as a background shadow in the front and the full logo in white on the back with a blue background.  On the card:
Dorn Pevsky, Operations Manager, dorn@brovalux-example.com
47215-K Harlow Ave. 9 #382
Pinecrest, IN 47912
555.604.2817, 888.555.4163

Updates
please include cell 555.318.6247
                                   
Thank you
If possible the fading logo on the front should be very subtle and light and lets look at centering that as well
thanks

```html
<!DOCTYPE html>
<html lang="en">
<head>
<meta charset="utf-8">
<title>brovalux business card</title>
<link rel="stylesheet" href="https://fonts.googleapis.com/css2?family=Source+Sans+3:wght@400;600;700&display=swap">
<style>
  :root {
    --page-bg: #e6e7ea;
    --navy: #0d2a5c;
    --blue-deep: #10346f;
    --blue-mid: #2f5f9e;
    --card-white: #f4f5f7;
    --card-grey: #dcdee2;
    --ink: #1e1f24;
    --accent: #3d8fd6;
    --mark-dark: #1a4a8c;
  }
  * { box-sizing: border-box; margin: 0; padding: 0; }
  html, body { width: 1200px; height: 900px; overflow: hidden; }
  body {
    background: var(--page-bg);
    font-family: "Source Sans 3", "Myriad Pro", sans-serif;
    position: relative;
  }
  .card {
    position: absolute;
    width: 540px;
    height: 309px;
    top: 296px;
    overflow: hidden;
    box-shadow: 0 6px 18px rgba(0,0,0,0.18);
  }
  /* Front: contact side */
  .card-front {
    left: 40px;
    background: linear-gradient(120deg, var(--card-white) 0%, #ffffff 45%, var(--card-grey) 100%);
    color: var(--ink);
  }
  .card-front .bg-disc {
    position: absolute;
    width: 250px; height: 250px;
    left: 145px; top: 30px;
    border-radius: 50%;
    background: rgba(255,255,255,0.55);
    box-shadow: 0 0 0 1px rgba(180,185,195,0.18);
  }
  .front-logo {
    position: absolute;
    left: 34px; top: 32px;
    display: flex; align-items: center; gap: 10px;
  }
  .front-logo .dot {
    width: 30px; height: 30px; border-radius: 50%;
    background: var(--mark-dark);
  }
  .front-logo .name {
    font-size: 30px; font-weight: 700; color: var(--mark-dark);
    letter-spacing: -0.5px; line-height: 1;
  }
  .address {
    position: absolute; left: 34px; top: 160px;
    font-size: 16px; line-height: 21px;
  }
  .phones {
    position: absolute; left: 34px; top: 214px;
    font-size: 16px; line-height: 21px;
  }
  .person {
    position: absolute; right: 30px; top: 182px;
    text-align: right;
  }
  .person .line { display: flex; align-items: baseline; justify-content: flex-end; gap: 6px; }
  .person .full-name { font-size: 19px; }
  .person .divider { width: 2px; height: 15px; background: var(--accent); align-self: center; }
  .person .role { font-size: 12.5px; }
  .person .email { font-size: 14px; font-weight: 600; margin-top: 4px; }

  /* Back: brand side */
  .card-back {
    left: 620px;
    background: linear-gradient(100deg, var(--navy) 0%, var(--blue-mid) 55%, var(--blue-deep) 100%);
    color: #ffffff;
  }
  .card-back .bg-disc {
    position: absolute;
    width: 270px; height: 270px;
    left: 110px; top: 6px;
    border-radius: 50%;
    background: rgba(255,255,255,0.22);
  }
  .back-logo {
    position: absolute;
    left: 0; right: 0; top: 110px;
    display: flex; align-items: center; justify-content: center; gap: 14px;
  }
  .back-logo .dot {
    width: 52px; height: 52px; border-radius: 50%; background: #ffffff;
  }
  .back-logo .name {
    font-size: 56px; font-weight: 700; line-height: 1; letter-spacing: -1px;
  }
  .web {
    position: absolute; left: 0; right: 0; top: 228px;
    text-align: center; font-size: 17px; letter-spacing: 0.3px;
  }
</style>
</head>
<body>
  <section class="card card-front" aria-label="Business card front">
    <div class="bg-disc"></div>
    <div class="front-logo">
      <span class="dot"></span>
      <span class="name">brovalux</span>
    </div>
    <p class="address">47215-K Harlow Ave. 9 #382<br>Pinecrest, IN 47912</p>
    <p class="phones">555.604.2817<br>888.555.4163<br>555.318.6247</p>
    <div class="person">
      <div class="line">
        <span class="full-name">Dorn Pevsky</span>
        <span class="divider"></span>
        <span class="role">Operations Manager</span>
      </div>
      <p class="email">dorn@brovalux-example.com</p>
    </div>
  </section>

  <section class="card card-back" aria-label="Business card back">
    <div class="bg-disc"></div>
    <div class="back-logo">
      <span class="dot"></span>
      <span class="name">brovalux</span>
    </div>
    <p class="web">www.brovalux-example.com</p>
  </section>
</body>
</html>
```